Sportlerurkunde designen
Zielgruppe
Der Wendelfurt Vierkampf ist eine Sportserie, die die 4 Ausdauersportarten Skilanglauf, Radfahren, Schwimmen und Laufen miteinander kombiniert. Dabei ist die Herausforderung diese 4 Wettkämpfe innerhalb von 12 Monaten zu absolvieren. Dafür hat der Vierkampf 4 feste Wettkämpfe die einmal pro Jahr stattfinden:
Graf Otmar Spur 50 km Skilanglauf
Brackwalder Heide Tour 300 km Radfahren
Tiefbach Kraulen 3,3 km Schwimmen
Solventa Halbwald Marathon 42,195 km Laufen
Absolviert der Athlet alle 4 Events innerhalb von 12 Monaten, bekommt er u.a. ein Wendelfurt Vierkampf Diplom, eine Urkunde auf der die Zeiten der Wettkämpfe vermerkt sind. Dieses möchten wir gerne designen lassen.
Aufgabenstellung
- Es ist eine hochwertige Sportserie, die eine anspruchsvolle Zielgruppe hat.
- Verwendung des aktuellen Wendelfurt Vierkampf Logos und die Logos der Wettkämpfe.
- Name der Wettkämpfe und Austragungsort
- Zeiten der 4 Wettkämpfe müssen mit abgebildet werden mit Veranstaltungsdatum,
- der Name der Athleten wird mit abgedruckt,
- Diplom wird unterschrieben,
- Größe des Diploms DIN A4
weitere Anregungen sind auf unserer Homepage www.wendelfurtvierkampf.de

```html
<!DOCTYPE html>
<html lang="de">
<head>
<meta charset="utf-8">
<title>Wendelfurt Vierkampf – Urkunde</title>
<link href="https://fonts.googleapis.com/css2?family=Ubuntu:wght@300;400;500&family=Caveat:wght@500&display=swap" rel="stylesheet">
<style>
  :root {
    --backdrop: #e4e4e2;
    --paper: #ffffff;
    --gold: #bfa23a;
    --gold-text: #b8962e;
    --ink: #353535;
    --muted: #555555;
    --map-deep: #f1d764;
    --map-light: #fbefa6;
    --brand-brown: #7d6d64;
    --pen: #1f2f8f;
  }
  * { margin: 0; padding: 0; box-sizing: border-box; }
  html, body { width: 1200px; height: 801px; overflow: hidden; }
  body { background: var(--backdrop); position: relative; font-family: "Ubuntu", sans-serif; color: var(--ink); }

  .certificate { position: absolute; top: 56px; width: 502px; height: 710px; background: var(--paper); box-shadow: 0 6px 18px rgba(0,0,0,.18); }
  .certificate--blank { left: 67px; }
  .certificate--filled { left: 634px; }
  .certificate::before, .certificate::after { content: ""; position: absolute; left: 0; right: 0; height: 9px; background: var(--gold); }
  .certificate::before { top: 0; }
  .certificate::after { bottom: 0; }

  .brand { position: absolute; top: 41px; left: 0; right: 0; text-align: center; z-index: 2; }
  .brand__dot { display: block; width: 36px; height: 36px; margin: 0 auto 18px; border-radius: 50%; background: var(--gold); }
  .brand__name { font-size: 15px; font-weight: 500; line-height: 18px; color: var(--ink); }

  .map { position: absolute; left: 51px; top: 130px; width: 393px; height: 524px; background: linear-gradient(160deg, var(--map-deep) 0%, var(--map-light) 60%, var(--map-deep) 100%); border-radius: 38% 44% 30% 36% / 22% 26% 18% 20%; z-index: 0; }

  .title { position: absolute; top: 165px; left: 0; right: 0; text-align: center; font-size: 41px; line-height: 1; font-weight: 400; letter-spacing: 10px; padding-left: 10px; z-index: 2; }

  .field { position: absolute; border-top: 1px solid var(--muted); z-index: 2; }
  .field__label { display: block; text-align: center; font-size: 6.5px; letter-spacing: .8px; text-transform: uppercase; color: var(--muted); margin-top: 4px; }
  .field__entry { position: absolute; bottom: 100%; left: 0; right: 0; text-align: center; font-family: "Caveat", cursive; font-weight: 500; color: var(--pen); line-height: 1; padding-bottom: 2px; white-space: nowrap; }
  .field__entry--name { font-size: 20px; }
  .field__entry--time { font-size: 18px; letter-spacing: 1px; }
  .field__entry--check { font-size: 12px; }

  .field--name { left: 163px; top: 246px; width: 196px; }
  .field--swim { left: 52px; top: 405px; width: 170px; }
  .field--ski { left: 268px; top: 405px; width: 171px; }
  .field--bike { left: 49px; top: 574px; width: 171px; }
  .field--run { left: 272px; top: 571px; width: 171px; }
  .field--verify { left: 44px; top: 658px; width: 227px; }

  .event { position: absolute; z-index: 2; }
  .event__km { font-size: 13px; letter-spacing: 1.5px; line-height: 13px; text-transform: uppercase; }
  .event__info { margin-top: 12px; font-size: 10.5px; font-weight: 300; letter-spacing: 1.4px; line-height: 12.8px; color: var(--gold-text); text-transform: uppercase; white-space: nowrap; }
  .event--swim { left: 123px; top: 304px; }
  .event--ski { left: 352px; top: 304px; }
  .event--bike { left: 131px; top: 475px; }
  .event--run { left: 347px; top: 474px; }

  .race-mark { position: absolute; z-index: 2; text-align: center; }
  .race-mark__shape { display: block; margin: 0 auto 5px; background: var(--brand-brown); }
  .race-mark__shape--circle { width: 34px; height: 34px; border-radius: 50%; }
  .race-mark__shape--square { width: 38px; height: 38px; }
  .race-mark__name { font-size: 8.5px; font-weight: 500; line-height: 10px; color: var(--brand-brown); text-transform: uppercase; }
  .race-mark--swim { left: 56px; top: 306px; width: 54px; }
  .race-mark--ski { left: 276px; top: 306px; width: 70px; }
  .race-mark--bike { left: 50px; top: 478px; width: 76px; }
  .race-mark--run { left: 268px; top: 472px; width: 74px; }
</style>
</head>
<body>

<section class="certificate certificate--blank">
  <div class="map" role="img" aria-label="Gelbe Landkarten-Silhouette als Hintergrund"></div>
  <header class="brand"><span class="brand__dot"></span><p class="brand__name">Wendelfurt<br>VIERKAMPF</p></header>
  <h1 class="title">URKUNDE</h1>
  <div class="field field--name"><span class="field__label">Name des Athleten</span></div>

  <div class="race-mark race-mark--swim"><span class="race-mark__shape race-mark__shape--circle"></span><p class="race-mark__name">Tiefbach Kraulen</p></div>
  <div class="event event--swim"><p class="event__km">3,3 km<br>Schwimmen</p><p class="event__info">27. August 2017<br>Tiefbacher See<br>Wendelstadt</p></div>
  <div class="field field--swim"><span class="field__label">Zeit des Athleten</span></div>

  <div class="race-mark race-mark--ski"><span class="race-mark__shape race-mark__shape--square"></span><p class="race-mark__name">Graf Otmar Spur</p></div>
  <div class="event event--ski"><p class="event__km">50 km<br>Skilanglauf</p><p class="event__info">3./4. Februar 2018<br>Otmarsgau</p></div>
  <div class="field field--ski"><span class="field__label">Zeit des Athleten</span></div>

  <div class="race-mark race-mark--bike"><span class="race-mark__shape race-mark__shape--circle"></span><p class="race-mark__name">Brackwalder Heide Tour</p></div>
  <div class="event event--bike"><p class="event__km">30 km<br>Radfahren</p><p class="event__info">25./26. Mai 2018<br>Brackwalde</p></div>
  <div class="field field--bike"><span class="field__label">Zeit des Athleten</span></div>

  <div class="race-mark race-mark--run"><span class="race-mark__shape race-mark__shape--square"></span><p class="race-mark__name">Solventa Halbwald Marathon</p></div>
  <div class="event event--run"><p class="event__km">42,195 km<br>Laufen</p><p class="event__info">29. Oktober 2017<br>Halbwald</p></div>
  <div class="field field--run"><span class="field__label">Zeit des Athleten</span></div>

  <div class="field field--verify"><span class="field__label">Verifiziert durch Prüfer</span></div>
</section>

<section class="certificate certificate--filled">
  <div class="map" role="img" aria-label="Gelbe Landkarten-Silhouette als Hintergrund"></div>
  <header class="brand"><span class="brand__dot"></span><p class="brand__name">Wendelfurt<br>VIERKAMPF</p></header>
  <h1 class="title">URKUNDE</h1>
  <div class="field field--name"><span class="field__entry field__entry--name">Erik Beispiel</span><span class="field__label">Name des Athleten</span></div>

  <div class="race-mark race-mark--swim"><span class="race-mark__shape race-mark__shape--circle"></span><p class="race-mark__name">Tiefbach Kraulen</p></div>
  <div class="event event--swim"><p class="event__km">3,3 km<br>Schwimmen</p><p class="event__info">27. August 2017<br>Tiefbacher See<br>Wendelstadt</p></div>
  <div class="field field--swim"><span class="field__entry field__entry--time">05:25:23 h</span><span class="field__label">Zeit des Athleten</span></div>

  <div class="race-mark race-mark--ski"><span class="race-mark__shape race-mark__shape--square"></span><p class="race-mark__name">Graf Otmar Spur</p></div>
  <div class="event event--ski"><p class="event__km">50 km<br>Skilanglauf</p><p class="event__info">3./4. Februar 2018<br>Otmarsgau</p></div>
  <div class="field field--ski"><span class="field__entry field__entry--time">05:25:23 h</span><span class="field__label">Zeit des Athleten</span></div>

  <div class="race-mark race-mark--bike"><span class="race-mark__shape race-mark__shape--circle"></span><p class="race-mark__name">Brackwalder Heide Tour</p></div>
  <div class="event event--bike"><p class="event__km">30 km<br>Radfahren</p><p class="event__info">25./26. Mai 2018<br>Brackwalde</p></div>
  <div class="field field--bike"><span class="field__entry field__entry--time">05:25:23 h</span><span class="field__label">Zeit des Athleten</span></div>

  <div class="race-mark race-mark--run"><span class="race-mark__shape race-mark__shape--square"></span><p class="race-mark__name">Solventa Halbwald Marathon</p></div>
  <div class="event event--run"><p class="event__km">42,195 km<br>Laufen</p><p class="event__info">29. Oktober 2017<br>Halbwald</p></div>
  <div class="field field--run"><span class="field__entry field__entry--time">05:25:23 h</span><span class="field__label">Zeit des Athleten</span></div>

  <div class="field field--verify"><span class="field__entry field__entry--check">Name Prüfer, 30.10.18, Halbwald</span><span class="field__label">Verifiziert durch Prüfer</span></div>
</section>

</body>
</html>
```